Tango Holiday Website Needs a Header Design

I'm looking for a talented designer to create an attractive header for my website: http://brightwaltzhaus.de/. I only want a Header Design. The website and everything else should stay the same.
We will be offering vacations for people who want to come to Tenerife to learn and dance Argentine tango. There will be lessons during the day and dancing during the evening. Tenerife is a warm and sunny destination.
The header should blend in well with the background and the images. The current dimentions fo the header is 960 x 160 pixels.
I like the design on a similar website: http://elvientobaile.de/.
Here are some images on google for tango holiday that might help: http://qk.ly/7xRm41P
I'm flexible with colours and am looking forward to your suggestions.
Tango dancers between the ages of 40 and 65
1 page

```html
<!DOCTYPE html>
<html lang="de">
<head>
<meta charset="utf-8">
<title>Brightwaltz Haus – Header</title>
<link rel="stylesheet" href="https://fonts.googleapis.com/css2?family=Pinyon+Script&family=Cormorant+SC:wght@600&family=Raleway:wght@400&display=swap">
<style>
  :root {
    --coral: #ff5252;
    --coral-dark: #ff4848;
    --coral-light: #ff6a6a;
    --paper: #ffffff;
    --ink: #111111;
    --silhouette: #0a0a0a;
  }
  html, body {
    margin: 0;
    padding: 0;
    overflow: hidden;
    background: var(--paper);
  }
  .site-header {
    position: relative;
    width: 1200px;
    height: 200px;
    overflow: hidden;
    background: var(--paper);
  }
  .backdrop {
    position: absolute;
    inset: 0;
  }
  .dancers {
    position: absolute;
    left: 125px;
    top: 8px;
    width: 150px;
    height: 192px;
    background: var(--silhouette);
    border-radius: 60px 60px 10px 10px;
  }
  .brand-name {
    position: absolute;
    left: 486px;
    top: 8px;
    margin: 0;
    font-family: "Pinyon Script", cursive;
    font-weight: 400;
    font-size: 76px;
    line-height: 1.2;
    color: var(--ink);
    white-space: nowrap;
  }
  .tagline {
    position: absolute;
    left: 479px;
    top: 100px;
    margin: 0;
    font-family: "Cormorant SC", serif;
    font-weight: 600;
    font-size: 24px;
    letter-spacing: 2px;
    color: var(--coral);
    white-space: nowrap;
  }
  .main-nav {
    position: absolute;
    top: 140px;
    left: 469px;
    height: 44px;
  }
  .nav-link {
    position: absolute;
    top: 0;
    height: 44px;
    display: flex;
    align-items: center;
    justify-content: center;
    background: var(--coral);
    color: var(--paper);
    font-family: "Raleway", sans-serif;
    font-size: 19px;
    text-decoration: none;
    border-radius: 2px;
    box-shadow: 0 1px 3px rgba(0,0,0,0.2);
  }
  .nav-home { left: 0; width: 152px; }
  .nav-providers { left: 161px; width: 252px; }
  .nav-contact { left: 426px; width: 148px; }
</style>
</head>
<body>
<header class="site-header">
  <svg class="backdrop" width="1200" height="200" viewBox="0 0 1200 200" aria-hidden="true">
    <polygon points="0,0 512,0 300,200 0,200" fill="var(--coral-light)"/>
    <polygon points="0,0 512,0 380,125" fill="var(--coral-dark)"/>
    <polygon points="0,60 0,200 140,200" fill="var(--coral-dark)"/>
    <polygon points="1200,50 1200,200 1050,200" fill="var(--coral)"/>
  </svg>

  <div class="dancers" role="img" aria-label="Schwarze Silhouette eines Tangopaares in enger Umarmung"></div>

  <h1 class="brand-name">Brightwaltz Haus</h1>
  <p class="tagline">Tango Holidays in Tenerife</p>

  <nav class="main-nav">
    <a class="nav-link nav-home" href="#">Homepage</a>
    <a class="nav-link nav-providers" href="#">Anbieter von Tango Reisen</a>
    <a class="nav-link nav-contact" href="#">Kontakt</a>
  </nav>
</header>
</body>
</html>
```